Flyer for Custom Home Builder!

my company is Harlow Ridge Homes, I am looking for a flyer that we can send via email to a customer, or print and hand out. I am thinking four pages so we could print this and fold it., possibly creating a folder. The name of the company is Harlow Ridge Homes our website is here www.harlowridgehomes-example.com. Some text you can use "Crafting luxury homes isn't just a job, it's our passion.
With meticulous attention to detail and an unwavering commitment to using the finest materials, Harlow Ridge Homes consistently delivers exceptional results that stand as a testament to our commitment to quality."

"Trust is the cornerstone of our foundation.
With a proven track record of delivering on our promises for over 16 years, we prioritize transparent communication and integrity throughout every step of the home-building journey".

you may need to obtain the photos here
https://files.example-share.net/f/k27pw4m8zrt03xq61bnv/h?key=48vn2c9q1x7mb5t0ekd3h&dl=0

Target Market(s)

We build homes for every wealthy clients, therefore the photos are extremely important

Industry/Entity Type

Construction.

Requirements
Must have
• clear larger photos

```html
<!DOCTYPE html>
<html lang="en">
<head>
<meta charset="utf-8">
<title>Harlow Ridge Homes – Brochure Spreads</title>
<link href="https://fonts.googleapis.com/css2?family=Montserrat:wght@700;800&family=Oswald:wght@300;400&family=Open+Sans:wght@400;600;700&display=swap" rel="stylesheet">
<style>
  :root{
    --bg:#e8e8ea;
    --paper:#ffffff;
    --ink:#2b2b2d;
    --muted:#6d6e72;
    --panel:#3e3f43;
    --panel-dark:#303134;
    --accent:#c8282e;
    --line:#d5d5d8;
  }
  *{margin:0;padding:0;box-sizing:border-box}
  html,body{width:720px;height:1200px;overflow:hidden}
  body{background:var(--bg);font-family:"Open Sans",Arial,sans-serif;color:var(--ink);position:relative}
  .spread{position:absolute;left:52px;width:616px;background:var(--paper);overflow:hidden}
  .spread--cover{top:70px;height:494px}
  .spread--inside{top:612px;height:520px}
  .page{position:absolute;top:0;width:308px;height:100%}
  .page--left{left:0}
  .page--right{left:308px}
  .photo{position:absolute}
  .brand{font-family:"Montserrat",Arial,sans-serif;font-weight:800;color:var(--ink);letter-spacing:1px;text-transform:uppercase;display:flex;align-items:center;gap:6px}
  .brand__square{width:8px;height:8px;background:var(--accent)}

  /* cover spread */
  .faded-hero{left:0;top:0;width:308px;height:130px;background:linear-gradient(180deg,#d9dadd 0%,#eceded 60%,#ffffff 100%)}
  .back-brand{position:absolute;left:24px;top:284px;font-size:13px}
  .contact{position:absolute;left:24px;top:316px;width:260px;list-style:none}
  .contact li{margin-bottom:9px}
  .contact__label{display:block;font-size:6.5px;font-weight:700;letter-spacing:1px;text-transform:uppercase;color:var(--ink)}
  .contact__value{display:block;font-size:6.5px;color:var(--muted);line-height:1.4}
  .front-brand{position:absolute;right:24px;top:60px;font-size:16px}
  .hero{left:170px;top:132px;width:250px;height:152px;background:linear-gradient(160deg,#e4e6e8 0%,#b9c3cb 40%,#6fa3c4 72%,#3f6f8e 100%)}
  .hero-detail{left:312px;top:284px;width:108px;height:98px;background:linear-gradient(180deg,#cfc6b9 0%,#a1907c 60%,#5d5247 100%)}
  .cover-panel{position:absolute;left:420px;top:128px;width:196px;height:354px;background:var(--panel)}
  .thumb-dusk{left:10px;top:10px;width:86px;height:84px;background:linear-gradient(180deg,#2b3c55 0%,#6a6f7a 55%,#c59a6a 100%)}
  .thumb-stairs{left:102px;top:10px;width:84px;height:84px;background:linear-gradient(135deg,#e3ddd3 0%,#a58e72 55%,#5a4d40 100%)}
  .tagline{position:absolute;left:14px;right:14px;top:118px;font-family:"Oswald",Arial,sans-serif;font-weight:300;color:#fff;text-transform:uppercase;text-align:right;line-height:1.05}
  .tagline__lead{display:block;font-size:30px;font-weight:400;letter-spacing:.5px}
  .tagline__rest{display:block;font-size:22px}
  .cover-url{position:absolute;right:14px;bottom:16px;font-size:7px;color:#d8d8da}

  /* inside spread */
  .intro{position:absolute;left:22px;top:22px;width:266px;font-size:6.5px;line-height:1.6;color:var(--muted)}
  .intro p{margin-bottom:7px}
  .gallery-panel{position:absolute;left:20px;top:190px;width:288px;height:306px;background:var(--panel-dark)}
  .g1{left:10px;top:10px;width:132px;height:60px;background:linear-gradient(135deg,#1f4fa6 0%,#3d7ad6 50%,#9fb8e0 100%)}
  .g2{left:150px;top:10px;width:128px;height:70px;background:linear-gradient(180deg,#dfe1e3 0%,#b8bcc0 60%,#7d8186 100%)}
  .g3{left:10px;top:76px;width:132px;height:60px;background:linear-gradient(180deg,#6c8fc2 0%,#8aa0a8 50%,#5b6b4c 100%)}
  .g4{left:10px;top:142px;width:132px;height:60px;background:linear-gradient(180deg,#42354f 0%,#8a5c6f 50%,#c27a5b 100%)}
  .work-card{position:absolute;left:152px;top:92px;width:136px;height:214px;background:var(--paper);padding:14px 12px}
  .work-card h2{font-family:"Montserrat",Arial,sans-serif;font-weight:700;font-size:11px;letter-spacing:1px;margin-bottom:8px}
  .work-card p{font-size:6.5px;line-height:1.6;color:var(--muted)}
  .work-card .cta{display:block;margin-top:6px;font-weight:700;color:var(--ink)}
  .interior{left:0;top:0;width:308px;height:520px;background:linear-gradient(180deg,#f1f0ec 0%,#dedbd4 35%,#9da68a 55%,#c9c1b3 75%,#8f8372 100%)}
</style>
</head>
<body>

<section class="spread spread--cover">
  <div class="page page--left">
    <div class="photo faded-hero" role="img" aria-label="Faded photo of a modern home exterior"></div>
    <div class="brand back-brand"><span class="brand__square"></span>Harlow Ridge Homes</div>
    <ul class="contact">
      <li><span class="contact__label">Phone</span><span class="contact__value">(512) 555-0148</span></li>
      <li><span class="contact__label">Email</span><span class="contact__value">info@harlowridgehomes-example.com</span></li>
      <li><span class="contact__label">Website</span><span class="contact__value">www.harlowridgehomes-example.com</span></li>
      <li><span class="contact__label">Open Hours</span><span class="contact__value">Mon – Fri, 8 AM – 5 PM</span></li>
      <li><span class="contact__label">Address</span><span class="contact__value">1820 Canyon Crest Road, Suite 210,<br>Austin, TX 78738</span></li>
    </ul>
  </div>
  <div class="page page--right">
    <div class="brand front-brand"><span class="brand__square"></span>Harlow Ridge Homes</div>
  </div>
  <div class="photo hero" role="img" aria-label="Photo of a luxury modern home with a pool"></div>
  <div class="photo hero-detail" role="img" aria-label="Photo of a warm interior living space"></div>
  <div class="cover-panel">
    <div class="photo thumb-dusk" role="img" aria-label="Photo of a home lit at dusk"></div>
    <div class="photo thumb-stairs" role="img" aria-label="Photo of a wooden staircase"></div>
    <h1 class="tagline">
      <span class="tagline__lead">Crafting</span>
      <span class="tagline__rest">Luxury homes<br>isn't just a job,<br>it's our passion</span>
    </h1>
    <span class="cover-url">www.harlowridgehomes-example.com</span>
  </div>
</section>

<section class="spread spread--inside">
  <div class="page page--left">
    <div class="intro">
      <p>At Harlow Ridge Homes, we specialize in creating exceptional, one-of-a-kind homes that are tailored to your vision and lifestyle. With meticulous attention to detail and an unwavering commitment to using the finest materials, Harlow Ridge Homes consistently delivers exceptional results that stand as a testament to our commitment to quality.</p>
      <p>Trust is the cornerstone of our foundation. With a proven track record of delivering on our promises for over 16 years, we prioritize transparent communication and integrity throughout every step of the home-building journey.</p>
      <p>From first sketch to final walkthrough, our team works beside you to bring every room, finish and view to life.</p>
    </div>
    <div class="gallery-panel">
      <div class="photo g1" role="img" aria-label="Photo of a home at night with blue lighting"></div>
      <div class="photo g2" role="img" aria-label="Photo of a bright modern kitchen"></div>
      <div class="photo g3" role="img" aria-label="Photo of a home exterior under blue sky"></div>
      <div class="photo g4" role="img" aria-label="Photo of a home at sunset"></div>
      <div class="work-card">
        <h2>WORK WITH US</h2>
        <p>From a detailed consultation to the final handover, our builders guide every choice with care. We listen first, plan clearly and build homes that reflect how you truly live.<span class="cta">Call us today!</span></p>
      </div>
    </div>
  </div>
  <div class="page page--right">
    <div class="photo interior" role="img" aria-label="Photo of a dining room with tall windows and garden view"></div>
  </div>
</section>

</body>
</html>
```